Website for Private Psychologist

DO NOT CONTACT ME PRIVATELY

I am a Psychologist offering psychotherapy for individuals and couples, and clinical consultation and training and education for mental and medical health professionals and agencies.

I need a redesign of my website

5 Pages (content is attached for each page)
Home
Jungian Psychotherapy
Clinical Consultation & Professional Development
Curriculum Vitae & Publications
Practice Policies and Forms

Designs can be based on these style websites
https://velmorcare.info; https://brantomind.org/; https://dorelhaskettpsychotherapy.com/

Minimalist Layout: Clean and uncluttered layout with generous white space, allowing the content and visuals to stand out'

Keep a linear, uncluttered, professional design.

Please use only royalty free images and google fonts. Please provide links to any stock images used to verify license.

private individual or couples seeking psychotherapy

Psychotherapy

5+ page

• No search feature

```html
<!DOCTYPE html>
<html lang="en">
<head>
<meta charset="utf-8">
<title>Velmor Depth Therapy</title>
<link rel="stylesheet" href="https://fonts.googleapis.com/css2?family=Playfair+Display:wght@600;700&family=Poppins:wght@400;500;600;700&display=swap">
<style>
:root{
  --navy:#1b2a63;
  --gold:#e6c07b;
  --gold-dark:#d9ad5f;
  --ink:#1d1d1f;
  --muted:#6b6b70;
  --soft:#f6f5f3;
  --cream:#fbf7ef;
  --white:#ffffff;
  --star:#f5b400;
}
*{box-sizing:border-box;margin:0;padding:0}
html,body{width:1200px;height:2710px;overflow:hidden}
body{font-family:"Poppins",sans-serif;color:var(--ink);background:var(--white);position:relative}
.abs{position:absolute}
.serif{font-family:"Playfair Display",serif;font-weight:700}
.btn{position:absolute;display:flex;align-items:center;justify-content:center;background:var(--gold);color:var(--white);font-weight:600;text-transform:uppercase;border-radius:4px;letter-spacing:.2px}
.label{position:absolute;color:var(--navy);font-weight:600;font-size:13px}
.body-text{position:absolute;color:var(--muted);font-size:12px;line-height:19px}
.photo{position:absolute}

/* top bar */
.topbar{position:absolute;left:0;top:0;width:1200px;height:33px;background:var(--navy);color:var(--white);font-size:11.5px}
.topbar .item{position:absolute;top:9px;display:flex;align-items:center;gap:8px}
.topbar b{font-weight:600}
.topbar .divider{position:absolute;top:6px;width:1px;height:22px;background:rgba(255,255,255,.5)}
.topbar .social{position:absolute;top:9px;width:14px;height:14px;border-radius:50%;border:1.5px solid var(--white)}

/* hero */
.hero{position:absolute;left:0;top:33px;width:1200px;height:557px;background:linear-gradient(180deg,#bcd0de 0%,#e7dccb 30%,#e8b768 52%,#b8762e 68%,#4a3116 100%)}
.logo{position:absolute;display:flex;align-items:center;gap:10px}
.logo .mark{width:40px;height:40px;border-radius:50%;border:2px solid var(--gold)}
.logo .name{font-weight:600;font-size:13px;line-height:15px;color:var(--navy)}
.nav{position:absolute;top:20px;font-size:9.5px;line-height:12px;color:var(--ink)}
.hero .welcome{position:absolute;left:113px;top:170px;color:var(--white);font-size:15px}
.hero h1{position:absolute;left:111px;top:200px;color:var(--white);font-size:55px;line-height:61px;font-family:"Playfair Display",serif;font-weight:700}
.play{position:absolute;left:931px;top:277px;width:74px;height:74px;border-radius:50%;border:1px solid rgba(255,255,255,.7);display:flex;align-items:center;justify-content:center}
.play span{width:50px;height:50px;border-radius:50%;background:var(--white);display:flex;align-items:center;justify-content:center}
.play-label{position:absolute;left:936px;top:360px;color:var(--white);font-size:10.5px}

/* about */
.about{position:absolute;left:0;top:590px;width:1200px;height:493px;background:var(--soft)}
.section-title{position:absolute;font-family:"Playfair Display",serif;font-weight:700;color:var(--ink)}

/* testimonials */
.testimonials{position:absolute;left:0;top:1553px;width:1200px;height:444px;background:var(--cream)}
.card{position:absolute;top:163px;width:315px;height:184px;background:var(--white)}
.card .avatar{position:absolute;left:20px;top:-34px;width:78px;height:78px;border-radius:50%;background:linear-gradient(160deg,#8b6a55,#3d4a66)}
.card .who{position:absolute;left:115px;top:17px;font-weight:600;font-size:12px;color:var(--ink)}
.card .stars{position:absolute;left:115px;top:37px;display:flex;gap:5px}
.card .quote{position:absolute;right:10px;top:-12px;font-family:"Playfair Display",serif;font-size:70px;line-height:70px;color:var(--gold);font-style:normal}
.card p{position:absolute;left:24px;top:79px;width:270px;font-size:10.5px;line-height:15.5px;color:var(--muted)}
.pager{position:absolute;top:379px;display:flex;align-items:center;gap:8px;font-size:12px;font-weight:500}

/* contact */
.list-dot{position:absolute;left:113px;width:15px;height:15px;border-radius:50%;background:var(--navy)}
.list-text{position:absolute;left:140px;font-size:13px;color:var(--ink)}
.appointment{position:absolute;left:694px;top:2048px;width:394px;height:374px;background:var(--gold)}
.field{position:absolute;height:40px;background:var(--white);border:1px solid #d9d2c4;font-size:10.5px;color:#9b9b9b;display:flex;align-items:center;padding-left:18px}
.field svg{position:absolute;right:12px;top:16px}

/* footer */
.footer{position:absolute;left:0;top:2485px;width:1200px;height:225px;background:var(--navy);color:var(--white)}
.footer .links{position:absolute;top:96px;font-size:11.5px}
.footer .rule{position:absolute;top:152px;height:1px;background:rgba(255,255,255,.5)}
.footer .sq{position:absolute;top:135px;width:33px;height:33px;background:var(--gold)}
.footer .copy{position:absolute;top:200px;left:0;width:1200px;text-align:center;font-size:10.5px}
</style>
</head>
<body>

<!-- top bar -->
<div class="topbar">
  <div class="item" style="left:366px">
    <svg width="15" height="11" viewBox="0 0 15 11"><rect x="0.5" y="0.5" width="14" height="10" rx="1" fill="var(--gold)"/><path d="M1 1l6.5 5 6.5-5" stroke="var(--navy)" fill="none"/></svg>
    <span>Email Us: <b>hello@velmorcare.info</b></span>
  </div>
  <div class="item" style="left:683px">
    <svg width="14" height="14" viewBox="0 0 24 24"><path fill="var(--gold)" d="M6.6 10.8a15.1 15.1 0 006.6 6.6l2.2-2.2c.3-.3.7-.4 1-.2 1.1.4 2.3.6 3.6.6.6 0 1 .4 1 1V20c0 .6-.4 1-1 1A17 17 0 013 4c0-.6.4-1 1-1h3.5c.6 0 1 .4 1 1 0 1.3.2 2.5.6 3.6.1.3 0 .7-.2 1z"/></svg>
    <span>Call Us: <b>(555) 210-4187</b></span>
  </div>
  <div class="divider" style="left:866px"></div>
  <svg class="abs" style="left:898px;top:7px" width="20" height="20" viewBox="0 0 20 20"><circle cx="8" cy="8" r="6" stroke="var(--gold)" stroke-width="1.8" fill="none"/><path d="M12.5 12.5l5 5" stroke="var(--gold)" stroke-width="1.8"/></svg>
  <div class="divider" style="left:954px"></div>
  <div class="social" style="left:978px;border-color:var(--gold)"></div>
  <div class="social" style="left:1007px;border-color:var(--gold)"></div>
  <div class="social" style="left:1039px;border-color:var(--gold)"></div>
  <div class="social" style="left:1072px;border-color:var(--gold)"></div>
</div>

<!-- hero -->
<section class="hero" role="img" aria-label="Photo: person with outstretched arms in a grass field at sunset">
  <div class="logo" style="left:113px;top:9px"><span class="mark"></span><span class="name">Velmor<br>Depth Therapy</span></div>
  <div class="nav" style="left:328px;top:26px">Jungian Psychotherapy</div>
  <div class="nav" style="left:480px">Clinical Consultation &amp;<br>Professional Development</div>
  <div class="nav" style="left:647px">Curriculum Vitae &amp;<br>Publications</div>
  <div class="nav" style="left:778px">Practice Policies<br>and Forms</div>
  <div class="btn" style="left:915px;top:11px;width:173px;height:45px;font-size:12.5px">Request &amp; Call</div>

  <div class="welcome">Welcome to Velmor Depth Therapy</div>
  <h1>You Deserve Peace<br>&amp; Freedom</h1>
  <div class="btn" style="left:113px;top:347px;width:170px;height:49px;font-size:12px">Leran More</div>

  <div class="play"><span><svg width="14" height="16" viewBox="0 0 14 16"><path d="M1 1l12 7-12 7z" fill="var(--navy)"/></svg></span></div>
  <div class="play-label">Watch Video</div>
</section>

<!-- about -->
<section class="about">
  <div class="photo" role="img" aria-label="Portrait photo of the psychologist" style="left:113px;top:62px;width:284px;height:337px;background:linear-gradient(160deg,#8a7a66,#3e3a36 55%,#1f1f22)"></div>
  <div class="photo" style="left:317px;top:270px;width:129px;height:160px;background:var(--white)"></div>
  <div class="photo" role="img" aria-label="Photo: woman sitting by the sea at sunset" style="left:323px;top:276px;width:123px;height:154px;background:linear-gradient(180deg,#e9b887,#c8a08a 45%,#7f8fa5)"></div>

  <div class="label" style="left:509px;top:99px">45 Years of Experience</div>
  <h2 class="section-title" style="left:509px;top:125px;font-size:34px">About Velmor Depth Therapy</h2>
  <p class="abs" style="left:510px;top:187px;width:445px;font-weight:600;font-size:12.5px;line-height:19px">Velmor Depth Therapy is a company with more than 45 years of experience offering top quality and highly efficient services.</p>
  <p class="body-text" style="left:510px;top:240px;width:445px">I am a California Licensed Psychologist with an office in the San Francisco Financial District offering psychotherapy for individuals and couples, and clinical consultation and training and education for mental and medical health professionals and agencies. All appointments are currently available via telehealth.</p>
  <div class="btn" style="left:509px;top:353px;width:122px;height:35px;font-size:9.5px">Learn More</div>
</section>

<!-- services -->
<section>
  <div class="label" style="left:113px;top:1183px">My Services</div>
  <h2 class="section-title" style="left:113px;top:1209px;font-size:34px;line-height:38px">Jungian Psychotherapy &amp;<br>Consultation</h2>
  <p class="body-text" style="left:113px;top:1300px;width:440px">I practice depth-oriented psychotherapy and tailor my approach to the individual or couple seeking treatment.&nbsp; I have experience treating a range of psychological issues including depression, anxiety, and relationship and job dissatisfaction as well as life transition issues such as college and graduate school stress, pre-marital counseling, and issues related to identity and sexuality.</p>
  <div class="btn" style="left:113px;top:1432px;width:122px;height:35px;font-size:9.5px">Learn More</div>
  <div class="photo" role="img" aria-label="Photo: distressed woman on a sofa with a therapist taking notes" style="left:683px;top:1146px;width:405px;height:345px;background:linear-gradient(135deg,#c9ccc9,#8a7e74 45%,#3c3a38)"></div>
</section>

<!-- testimonials -->
<section class="testimonials">
  <div class="label" style="left:0;width:1200px;text-align:center;top:52px">Testimonials</div>
  <h2 class="section-title" style="left:0;width:1200px;text-align:center;top:76px;font-size:34px">Client Testimonials</h2>

  <div class="card" style="left:113px">
    <div class="avatar" role="img" aria-label="Client photo"></div>
    <div class="who">ARLO PENNICK</div>
    <div class="stars"><svg width="104" height="16" viewBox="0 0 104 16"><g fill="var(--star)"><path id="st" d="M8 0l2.4 5.1 5.6.7-4.1 3.8 1 5.5L8 12.4 3.1 15.1l1-5.5L0 5.8l5.6-.7z"/><use href="#st" x="22"/><use href="#st" x="44"/><use href="#st" x="66"/><use href="#st" x="88"/></g></svg></div>
    <div class="quote">”</div>
    <p>Lorem ipsum dolor sit amet, consectetur adipiscing elit, sed do eiusmod tempor incididunt ut labore et dolore magna aliqua. Quis ipsum suspendisse ultrices gravida. Risus commodo viverra maecenas accumsan lacus vel facilisis.</p>
  </div>
  <div class="card" style="left:443px">
    <div class="avatar" role="img" aria-label="Client photo"></div>
    <div class="who">ROSS DELACEY</div>
    <div class="stars"><svg width="104" height="16" viewBox="0 0 104 16"><g fill="var(--star)"><use href="#st"/><use href="#st" x="22"/><use href="#st" x="44"/><use href="#st" x="66"/><use href="#st" x="88"/></g></svg></div>
    <div class="quote">”</div>
    <p>Lorem ipsum dolor sit amet, consectetur adipiscing elit, sed do eiusmod tempor incididunt ut labore et dolore magna aliqua. Quis ipsum suspendisse ultrices gravida. Risus commodo viverra maecenas accumsan lacus vel facilisis.</p>
  </div>
  <div class="card" style="left:773px">
    <div class="avatar" role="img" aria-label="Client photo"></div>
    <div class="who">OWEN STRADE</div>
    <div class="stars"><svg width="104" height="16" viewBox="0 0 104 16"><g fill="var(--star)"><use href="#st"/><use href="#st" x="22"/><use href="#st" x="44"/><use href="#st" x="66"/><use href="#st" x="88"/></g></svg></div>
    <div class="quote">”</div>
    <p>Lorem ipsum dolor sit amet, consectetur adipiscing elit, sed do eiusmod tempor incididunt ut labore et dolore magna aliqua. Quis ipsum suspendisse ultrices gravida. Risus commodo viverra maecenas accumsan lacus vel facilisis.</p>
  </div>

  <div class="pager" style="left:475px;color:var(--gold)"><svg width="30" height="10" viewBox="0 0 30 10"><path d="M29 5H1m4-4L1 5l4 4" stroke="var(--gold)" fill="none"/></svg>PREVIOUS</div>
  <div class="pager" style="left:632px;color:var(--navy)">NEXT<svg width="30" height="10" viewBox="0 0 30 10"><path d="M1 5h28m-4-4l4 4-4 4" stroke="var(--navy)" fill="none"/></svg></div>
</section>

<!-- contact -->
<section>
  <div class="label" style="left:113px;top:2061px">Get In Touch</div>
  <h2 class="section-title" style="left:113px;top:2086px;font-size:34px">Contact Us</h2>
  <p class="body-text" style="left:113px;top:2144px;width:480px">Interdum et malesuada fames ac ante ipsum primis in faucibus. Sed eu mauris sit amet neque porta pharetra. Ut fringilla laoreet rutrum. Morbi commodo ex a nisl feugiat interdum. Sed nec felis vel mi pellentesque finibus.</p>
  <span class="list-dot" style="top:2228px"></span><span class="list-text" style="top:2225px">51 Street, Network City, NYPD</span>
  <span class="list-dot" style="top:2261px"></span><span class="list-text" style="top:2258px">Which don't Look Even Slightly Believable</span>
  <span class="list-dot" style="top:2295px"></span><span class="list-text" style="top:2292px">555 304 7719 402</span>
  <div class="abs" style="left:113px;top:2338px;width:49px;height:49px;border-radius:50%;background:var(--gold);display:flex;align-items:center;justify-content:center">
    <svg width="18" height="18" viewBox="0 0 24 24"><path fill="var(--white)" d="M6.6 10.8a15.1 15.1 0 006.6 6.6l2.2-2.2c.3-.3.7-.4 1-.2 1.1.4 2.3.6 3.6.6.6 0 1 .4 1 1V20c0 .6-.4 1-1 1A17 17 0 013 4c0-.6.4-1 1-1h3.5c.6 0 1 .4 1 1 0 1.3.2 2.5.6 3.6.1.3 0 .7-.2 1z"/></svg>
  </div>
  <div class="abs" style="left:183px;top:2342px;font-weight:600;font-size:13px">Quick Support Number</div>
  <div class="abs" style="left:183px;top:2361px;font-weight:600;font-size:18px">(555) 210-4187</div>

  <div class="appointment">
    <h2 class="section-title" style="left:30px;top:48px;font-size:33px">Make An Appointment</h2>
    <div class="field" style="left:30px;top:105px;width:161px">Name</div>
    <div class="field" style="left:203px;top:105px;width:161px">Eamil</div>
    <div class="field" style="left:30px;top:157px;width:334px">Select Service<svg width="9" height="6" viewBox="0 0 9 6"><path d="M1 1l3.5 3.5L8 1" stroke="#888" fill="none"/></svg></div>
    <div class="field" style="left:30px;top:208px;width:161px">Phone</div>
    <div class="field" style="left:203px;top:208px;width:161px">Select Date<svg width="9" height="6" viewBox="0 0 9 6"><path d="M1 1l3.5 3.5L8 1" stroke="#888" fill="none"/></svg></div>
    <div class="btn" style="left:31px;top:266px;width:197px;height:50px;background:var(--navy);font-size:12.5px">Book An Appointment</div>
  </div>
</section>

<!-- footer -->
<footer class="footer">
  <div class="abs" style="left:577px;top:22px;width:46px;height:46px;border-radius:50%;border:2px solid var(--gold)"></div>
  <div class="links" style="left:164px">Jungian Psychotherapy</div>
  <div class="links" style="left:337px">Clinical Consultation &amp; Professional Development</div>
  <div class="links" style="left:659px">Curriculum Vitae &amp; Publications</div>
  <div class="links" style="left:877px">Practice Policies and Forms</div>
  <div class="rule" style="left:0;width:496px"></div>
  <div class="rule" style="left:704px;width:496px"></div>
  <div class="sq" style="left:513px" aria-label="Social link"></div>
  <div class="sq" style="left:560px" aria-label="Social link"></div>
  <div class="sq" style="left:607px" aria-label="Social link"></div>
  <div class="sq" style="left:654px" aria-label="Social link"></div>
  <div class="copy">Copyright © 2010-2023 All rights reserved.</div>
</footer>

</body>
</html>
```